IT Security Company Website

We would like to create a new look for our current company site veltrom.io. The company offercyber security services for banks, goverment etc. Therefore a very professional look is important. We need at least 2 pages designed.

Target Market(s)

B2B

Coding

Coded - Design and coding required

Number of Pages Required

1 page

```html
<!DOCTYPE html>
<html lang="en">
<head>
<meta charset="utf-8">
<title>Veltrom – Cyber Threat Intelligence</title>
<link href="https://fonts.googleapis.com/css2?family=Catamaran:wght@400;500;600;700;800&display=swap" rel="stylesheet">
<style>
:root{
  --gold:#f2c230;
  --gold-soft:#f6d56a;
  --ink:#15171c;
  --text:#4a4d55;
  --muted:#8b8e96;
  --line:#e6e6e6;
  --night:#0b0f1a;
  --footer:#1d1e22;
  --light:#f4f4f4;
  --white:#ffffff;
}
*{box-sizing:border-box;margin:0;padding:0}
html,body{width:1200px;height:5150px;overflow:hidden}
body{font-family:"Catamaran",sans-serif;color:var(--text);background:var(--white);font-size:14px;line-height:1.6}
section,header,footer{position:relative;width:1200px;overflow:hidden}
.eyebrow{font-size:10px;letter-spacing:4px;color:var(--gold);text-transform:uppercase;font-weight:600;display:flex;align-items:center;justify-content:center;gap:12px}
.eyebrow::before,.eyebrow::after{content:"";width:22px;height:1px;background:var(--gold);opacity:.6}
.eyebrow.left{justify-content:flex-start}
.eyebrow.left::before{display:none}
.title{font-weight:800;color:var(--ink);text-transform:uppercase;font-size:28px;line-height:1.25;letter-spacing:.5px}
.center{text-align:center}
.btn{display:inline-block;background:var(--gold);color:var(--white);font-size:10px;letter-spacing:1.5px;text-transform:uppercase;font-weight:700;border-radius:20px;padding:9px 22px;text-decoration:none}
.btn.dark{background:var(--ink)}
/* Hero */
.hero{height:570px;background:radial-gradient(ellipse at 75% 65%,#1f4a7a 0%,#0e1d3a 30%,#070a14 65%),#070a14;color:var(--white)}
.hero-art{position:absolute;inset:0;background:radial-gradient(ellipse at 30% 95%,rgba(40,140,200,.45),transparent 40%),radial-gradient(ellipse at 88% 40%,rgba(60,110,200,.35),transparent 35%)}
.nav{position:absolute;top:30px;left:72px;right:72px;display:flex;align-items:center;height:34px}
.logo{font-size:30px;font-weight:400;letter-spacing:1px;color:var(--white)}
.logo span{color:var(--gold)}
.nav-links{display:flex;gap:26px;margin-left:auto;margin-right:26px;font-size:10px;font-weight:600;letter-spacing:.5px;text-transform:uppercase}
.nav-links a{color:var(--white);text-decoration:none;padding:6px 0}
.nav-links a.active{color:var(--gold);border-bottom:2px solid var(--gold)}
.nav .btn{padding:8px 18px}
.hero-copy{position:absolute;top:188px;left:0;right:0;text-align:center}
.hero-copy .kicker{font-size:11px;letter-spacing:4px;text-transform:uppercase}
.hero-copy h1{font-size:40px;font-weight:800;line-height:1.15;margin-top:10px;text-transform:uppercase}
.hero-copy p{font-size:12px;margin:12px 0 18px}
.scroll-down{position:absolute;left:582px;top:510px;width:36px;height:36px;border-radius:50%;background:rgba(255,255,255,.12)}
/* About */
.about{height:480px}
.about-photo{position:absolute;left:72px;top:78px;width:516px;height:322px;background:linear-gradient(135deg,#5c636d,#1d2228 70%)}
.play{position:absolute;left:556px;top:206px;width:64px;height:64px;border-radius:50%;background:var(--white);box-shadow:0 4px 18px rgba(0,0,0,.15);display:flex;align-items:center;justify-content:center}
.about-copy{position:absolute;left:660px;top:78px;width:400px}
.about-copy .title{margin:10px 0 16px}
.about-copy p{font-size:12px;margin-bottom:12px}
/* Reporting */
.reporting{height:312px}
.reporting .rule{position:absolute;top:0;left:0;right:0;border-top:1px solid var(--line)}
.reporting .eyebrow{position:absolute;top:-8px;left:0;right:0}
.reporting .eyebrow span{background:var(--white);padding:0 12px}
.features{position:absolute;top:80px;left:72px;right:72px;display:grid;grid-template-columns:repeat(4,1fr);text-align:center}
.feat-icon{width:80px;height:80px;border-radius:50%;background:#f1f1f1;margin:0 auto 22px;display:flex;align-items:center;justify-content:center;box-shadow:0 4px 12px rgba(0,0,0,.06)}
.feat-icon.on{background:var(--gold)}
.feat h3{font-size:11px;font-weight:700;color:var(--ink);text-transform:uppercase}
.feat.on h3{color:var(--gold)}
.feat p{font-size:11px}
/* CISO */
.ciso{height:490px;display:flex}
.ciso-copy{width:600px;background:var(--light);padding:80px 80px 0 132px}
.ciso-copy .title{margin:10px 0 12px}
.ciso-copy p{font-size:11px;margin-bottom:10px;line-height:1.6}
.ciso-photo{width:600px;background:radial-gradient(ellipse at 70% 45%,#c99a7c 0%,#3d5a78 30%,#10233a 65%)}
/* Risks */
.risks{height:562px;padding-top:78px}
.risks .title{margin:8px 0 10px}
.risks .sub{font-size:12px;width:500px;margin:0 auto}
.risk-row{display:flex;justify-content:center;gap:54px;margin-top:46px}
.risk{text-align:center;width:72px}
.risk .feat-icon{width:72px;height:72px;margin-bottom:14px}
.risk span{font-size:9px;letter-spacing:1px;text-transform:uppercase;color:var(--muted)}
.risk.on span{color:var(--ink)}
.risks h4{font-size:16px;font-weight:700;color:var(--ink);margin-top:44px}
.risks .detail{font-size:11px;width:850px;margin:6px auto 0}
/* Testimonials */
.testimonials{height:514px;background:radial-gradient(ellipse at 50% 110%,#1a5a8a 0%,#0b2444 35%,#060b16 75%);color:var(--white);padding-top:80px}
.testimonials .title{color:var(--white);margin-top:8px}
.avatar{width:68px;height:68px;border-radius:50%;background:radial-gradient(circle,#c99f85,#6d4b3b);border:3px solid var(--gold);margin:60px auto 20px}
.quote{font-size:15px;width:700px;margin:0 auto;line-height:1.6}
.stars{color:var(--gold);letter-spacing:6px;margin-top:6px;font-size:16px}
.author{font-size:12px;line-height:1.5;margin-top:4px}
.arrow{position:absolute;top:2720px}
/* Dots */
.dots{height:482px;padding-top:86px}
.dots .title{margin:8px 0 10px}
.dots .sub{font-size:11px;width:490px;margin:0 auto}
.dot-row{display:grid;grid-template-columns:repeat(3,1fr);margin:64px 72px 0;text-align:center}
.dot-icon{width:76px;height:76px;border-radius:50%;background:var(--ink);margin:0 auto 8px;display:flex;align-items:center;justify-content:center;color:var(--white);font-size:22px;font-weight:700}
.dot-icon.on{background:var(--white);color:var(--ink);border:4px solid var(--gold)}
.dot-num{font-size:10px;color:var(--gold);font-weight:600}
.dot h3{font-size:12px;font-weight:700;color:var(--ink);text-transform:uppercase;line-height:1.3}
.dot.on h3{color:var(--gold);font-weight:500}
.dot p{font-size:11px;width:320px;margin:6px auto 0}
/* References */
.refs{height:260px;background:linear-gradient(var(--white),var(--light))}
.refs .eyebrow{padding-top:0}
.ref-row{position:absolute;top:90px;left:72px;right:72px;display:flex;align-items:center;justify-content:space-between}
.ref{width:232px;height:80px;display:flex;align-items:center;justify-content:center;gap:8px;font-size:18px;font-weight:700;color:var(--ink)}
.ref.card{background:var(--white);box-shadow:0 4px 16px rgba(0,0,0,.1)}
.ref i{width:16px;height:16px;background:var(--ink);display:inline-block}
.chev{color:var(--muted);font-size:26px;font-weight:300}
/* News */
.news{height:690px;background:var(--light);padding-top:80px}
.news .title{margin-top:8px}
.cards{display:grid;grid-template-columns:repeat(3,336px);gap:24px;margin:46px 72px 0}
.card{background:var(--white)}
.card.on{box-shadow:0 6px 22px rgba(0,0,0,.12)}
.card-img{height:158px;position:relative}
.card-body{padding:22px 24px 26px}
.meta{font-size:10px;color:var(--gold)}
.meta b{color:var(--muted);font-weight:400}
.card h3{font-size:13px;font-weight:700;color:var(--ink);line-height:1.4;margin:10px 0 6px}
.card.on h3{color:var(--gold)}
.card p{font-size:11px}
.date{font-size:9px;color:#c3c3c3;margin-top:14px}
.readmore{font-size:10px;color:var(--gold);margin-top:14px;display:block}
.plus{position:absolute;left:148px;top:60px;width:38px;height:38px;border-radius:50%;background:var(--gold);color:var(--white);display:flex;align-items:center;justify-content:center;font-size:20px}
.news .center-btn{text-align:center;margin-top:44px}
/* Contact */
.contact{height:376px;display:flex}
.contact-art{width:600px;background:radial-gradient(ellipse at 55% 55%,#2f79b8 0%,#0e2e55 35%,#03070f 70%)}
.contact-copy{width:600px;padding:84px 0 0 60px}
.contact-copy .title{margin:10px 0 12px}
.contact-copy p{font-size:11px;width:400px}
.contact-copy .actions{display:flex;gap:12px;margin-top:22px}
/* Footer */
.footer{height:414px;background:var(--footer);color:#cfcfcf}
.f-brand{position:absolute;left:72px;top:70px;width:180px;text-align:center}
.f-brand .logo{font-size:42px}
.f-brand small{display:block;font-size:11px;color:var(--muted);margin:4px 0 10px}
.socials{display:flex;gap:10px;justify-content:center}
.socials i{width:26px;height:26px;border-radius:50%;background:#2c2d32;display:block}
.f-col{position:absolute;top:88px;font-size:11px;line-height:2}
.f-col h5{font-size:10px;letter-spacing:1.5px;color:var(--muted);font-weight:600;text-transform:uppercase;margin-bottom:14px}
.f-col a{display:block;color:#e2e2e2;text-decoration:none}
.f-col a.active{color:var(--gold)}
.f-col .lab{color:var(--muted);line-height:1.4;margin-top:6px}
.f-col .val{line-height:1.4;color:#e2e2e2}
.newsletter-field{margin-top:10px;width:244px;height:36px;border:1px solid #3a3b40;border-radius:18px;display:flex;align-items:center;justify-content:space-between;padding:0 18px;color:#6b6d72;font-size:10px}
.f-bottom{position:absolute;left:72px;right:72px;top:364px;display:flex;justify-content:space-between;font-size:9px;color:var(--muted)}
.f-bottom b{color:#e2e2e2;font-weight:600;letter-spacing:1px;margin-left:16px}
</style>
</head>
<body>

<header class="hero">
  <div class="hero-art" role="img" aria-label="Dark digital globe with glowing network lines"></div>
  <nav class="nav">
    <div class="logo">VELT<span>ROM</span></div>
    <div class="nav-links">
      <a class="active" href="#">Home</a><a href="#">About</a><a href="#">Q&amp;A</a><a href="#">Pricing</a><a href="#">Partner Program</a><a href="#">Resources</a><a href="#">Contact Us</a>
    </div>
    <a class="btn" href="#">Arrange a live demo</a>
  </nav>
  <div class="hero-copy">
    <div class="kicker">Find exposed data in the darknet</div>
    <h1>Defend against cyber-attacks<br>before they happen</h1>
    <p>Cyber Threat Intelligence made for swiss banks. Priced for MSSP.</p>
    <a class="btn" href="#">Explore more</a>
  </div>
  <div class="scroll-down"><svg width="36" height="36" viewBox="0 0 36 36"><path d="M14 16l4 4 4-4" fill="none" stroke="#fff" stroke-width="1.5"/></svg></div>
</header>

<section class="about">
  <div class="about-photo" role="img" aria-label="Padlock resting on a laptop keyboard"></div>
  <div class="play"><svg width="20" height="20" viewBox="0 0 20 20"><path d="M6 3l10 7-10 7z" fill="none" stroke="#f2c230" stroke-width="1.6"/></svg></div>
  <div class="about-copy">
    <div class="eyebrow left">About</div>
    <h2 class="title">Created for swiss banks,<br>priced for MSSP</h2>
    <p>Veltrom helps you understand when, where and how stolen or accidentally leaked information in dark web markets, forums, botnet logs, IRC, social media and other sources is exposed.</p>
    <p>Veltrom’s alerting service can also detect threats before they turn into incidents. Veltrom offers AI-driven dark web analysis, real-time threat alerts and pre-Attack threat indicators. Setup in minutes you will receive instant access to real-time reporting.</p>
    <a class="btn" href="#">More about us</a>
  </div>
</section>

<section class="reporting">
  <div class="rule"></div>
  <div class="eyebrow"><span>Real-time reporting</span></div>
  <div class="features">
    <div class="feat"><div class="feat-icon"><svg width="30" height="30" viewBox="0 0 30 30" fill="none" stroke="#555" stroke-width="1.4"><circle cx="15" cy="15" r="10"/><path d="M5 15h20M15 5v20"/></svg></div><h3>Infrastructure exposure</h3><p>IOT, Git, Nimbus, Codeshelf &amp; more</p></div>
    <div class="feat"><div class="feat-icon"><svg width="30" height="30" viewBox="0 0 30 30" fill="none" stroke="#555" stroke-width="1.4"><circle cx="15" cy="11" r="5"/><path d="M6 25c1-6 17-6 18 0"/></svg></div><h3>People exposure</h3><p>Social media monitoring</p></div>
    <div class="feat on"><div class="feat-icon on"><svg width="30" height="30" viewBox="0 0 30 30" fill="none" stroke="#fff" stroke-width="1.4"><rect x="6" y="5" width="18" height="20"/><path d="M10 10h10M10 15h10M10 20h6"/></svg></div><h3>Ransomware exposure</h3><p>leak &amp; credential monitoring</p></div>
    <div class="feat"><div class="feat-icon"><svg width="30" height="30" viewBox="0 0 30 30" fill="none" stroke="#555" stroke-width="1.4"><rect x="6" y="6" width="18" height="18"/><path d="M6 12h18M12 12v12"/></svg></div><h3>Attack prevention</h3><p>domain and certificate monitoring</p></div>
  </div>
</section>

<section class="ciso">
  <div class="ciso-copy">
    <div class="eyebrow left">The CISO’s solution</div>
    <h2 class="title">Forewarned is forearmed</h2>
    <p>Veltrom helps you understand when, where and how stolen or accidentally leaked information is exposed. Veltrom’s alerting service can also detect threats before they turn into incidents.</p>
    <p>There are certain indicators that can be measured. Before an attack takes place, hackers often reserve similar domain names (typosquatting), they spoof profiles in social media like Linkora or they exchange information about targets in hacker forums. Veltrom monitors these activities using “Social Media Monitoring”, “Domain Monitoring” and the “Hacker Forum Monitoring”.</p>
    <p>Veltrom’s Intelligent Filters and Machine Learning find the real risks among the vast amount of data we collect through human and machine intelligence.</p>
    <a class="btn" href="#" style="margin-top:8px">Partner program</a>
  </div>
  <div class="ciso-photo" role="img" aria-label="Hand reaching toward a glowing holographic data interface"></div>
</section>

<section class="risks center">
  <div class="eyebrow">Risks</div>
  <h2 class="title">Mitigated with Veltrom</h2>
  <p class="sub">A web dashboard for coaches and dietitians paired with an app for athletes providing data on athlete nutrition status and energy expenditure.</p>
  <div class="risk-row">
    <div class="risk on"><div class="feat-icon on"><svg width="26" height="26" viewBox="0 0 26 26" fill="none" stroke="#fff" stroke-width="1.4"><rect x="4" y="5" width="18" height="16"/><path d="M4 6l9 7 9-7"/></svg></div><span>Phishing</span></div>
    <div class="risk"><div class="feat-icon"><svg width="26" height="26" viewBox="0 0 26 26" fill="none" stroke="#555" stroke-width="1.4"><circle cx="13" cy="13" r="6"/><path d="M13 3v4M13 19v4M3 13h4M19 13h4"/></svg></div><span>Infrastructure</span></div>
    <div class="risk"><div class="feat-icon"><svg width="26" height="26" viewBox="0 0 26 26" fill="none" stroke="#555" stroke-width="1.4"><rect x="4" y="6" width="18" height="14"/><path d="M4 10h18"/></svg></div><span>Ransomware</span></div>
    <div class="risk"><div class="feat-icon"><svg width="26" height="26" viewBox="0 0 26 26" fill="none" stroke="#555" stroke-width="1.4"><rect x="4" y="7" width="18" height="13"/><path d="M4 8l9 6 9-6"/></svg></div><span>Darknet</span></div>
    <div class="risk"><div class="feat-icon"><svg width="26" height="26" viewBox="0 0 26 26" fill="none" stroke="#555" stroke-width="1.4"><rect x="5" y="4" width="16" height="18"/><path d="M8 9h10M8 13h10M8 17h10"/></svg></div><span>Spoofing</span></div>
    <div class="risk"><div class="feat-icon"><svg width="26" height="26" viewBox="0 0 26 26" fill="none" stroke="#555" stroke-width="1.4"><circle cx="10" cy="9" r="4"/><path d="M3 22c1-6 13-6 14 0M17 14l5 5"/></svg></div><span>Employee</span></div>
    <div class="risk"><div class="feat-icon"><svg width="26" height="26" viewBox="0 0 26 26" fill="none" stroke="#555" stroke-width="1.4"><rect x="4" y="4" width="18" height="18"/><path d="M9 9h8v8H9z"/></svg></div><span>Data</span></div>
  </div>
  <h4>Prevent phishing</h4>
  <p class="detail">We monitor all new domain registrations (ccTLDs, gTLDs, uTLD, sTLD). In doing so, we also record typical typosquatting techniques. Veltrom automatically analyzes domains that appear suspicious, capturing key properties such as WHOIS , geolocation, open web services, screenshots, similarity to the original site (AI analysis) etc. With our certificate log monitoring service you will also detect scammers using the same name on a SSL certificate as your protected asset.</p>
</section>

<section class="testimonials center" role="group" aria-label="Testimonials">
  <div class="eyebrow">Testimonials</div>
  <h2 class="title">What our clients say</h2>
  <div class="avatar" role="img" aria-label="Client portrait"></div>
  <p class="quote">“Lorem Ipsum is simply dummy text of the printing and typesetting industry. Lorem Ipsum has been the industry’s standard dummy text ever since the 1500s, when an unknown printer took a galley of type and scrambled it to make a type specimen book.”</p>
  <div class="stars">☆☆☆☆☆</div>
  <div class="author">Jonas<br>Berger</div>
  <svg style="position:absolute;left:160px;top:310px" width="14" height="24" viewBox="0 0 14 24"><path d="M11 2L3 12l8 10" fill="none" stroke="#9aa" stroke-width="1.5"/></svg>
  <svg style="position:absolute;right:160px;top:310px" width="14" height="24" viewBox="0 0 14 24"><path d="M3 2l8 10-8 10" fill="none" stroke="#9aa" stroke-width="1.5"/></svg>
</section>

<section class="dots center">
  <div class="eyebrow">Veltrom is different</div>
  <h2 class="title">We connect the dots!</h2>
  <p class="sub">The whole of the information generated by artificial intelligence is greater than the sum of the individual pieces of information added together. We connect the dots</p>
  <div class="dot-row">
    <div class="dot"><div class="dot-icon"><svg width="28" height="28" viewBox="0 0 28 28" fill="none" stroke="#fff" stroke-width="1.4"><path d="M14 4l9 4v6c0 6-4 9-9 11-5-2-9-5-9-11V8z"/></svg></div><div class="dot-num">01</div><h3>Security</h3><p>Most affordable CTI data in the market - tailored for MSSP’s and security vendors</p></div>
    <div class="dot on"><div class="dot-icon on">02</div><div class="dot-num">&nbsp;</div><h3>Analysis</h3><p>Intelligent analysis of the information and the most flexible search option of any tool out there</p></div>
    <div class="dot"><div class="dot-icon"><svg width="28" height="28" viewBox="0 0 28 28" fill="none" stroke="#fff" stroke-width="1.4"><ellipse cx="14" cy="7" rx="8" ry="3"/><path d="M6 7v14c0 2 16 2 16 0V7M6 14c0 2 16 2 16 0"/></svg></div><div class="dot-num">03</div><h3>Data</h3><p>Access to historical data and also real live view in Darknet and Deep Web</p></div>
  </div>
</section>

<section class="refs">
  <div class="eyebrow" style="position:absolute;top:-8px;left:0;right:0">References</div>
  <div class="ref-row">
    <span class="chev">‹</span>
    <div class="ref"><i></i>Northwall</div>
    <div class="ref card">Alvena Bank</div>
    <div class="ref"><i></i>Helvetic Secure</div>
    <div class="ref">Grisonguard</div>
    <span class="chev">›</span>
  </div>
</section>

<section class="news">
  <div class="eyebrow">Resources</div>
  <h2 class="title center">Cyber threat intelligence news</h2>
  <div class="cards">
    <article class="card"><div class="card-img" role="img" aria-label="Blue light streaks of data in motion" style="background:linear-gradient(135deg,#0d2c5a,#3b8fd8 50%,#0a1630)"></div><div class="card-body"><div class="meta">by Admin <b>|</b> News</div><h3>Lorem ipsum dolor sit amet, consectetur adipiscing elit.</h3><p>Lorem Ipsum is simply dummy text of the printing and typesetting industry.</p><div class="date">Sep 10, 2021</div></div></article>
    <article class="card on"><div class="card-img" role="img" aria-label="Dark office scene" style="background:linear-gradient(135deg,#2a2b2e,#4b4c50)"><span class="plus">+</span></div><div class="card-body"><div class="meta">by Admin <b>|</b> Press</div><h3>Phasellus iaculis eros eu commodo mattis. Ut placerat tincidunt mi</h3><p>Lorem Ipsum is simply dummy text of the printing and typesetting industry.</p><span class="readmore">Read More ›</span></div></article>
    <article class="card"><div class="card-img" role="img" aria-label="Purple blurred code on a screen" style="background:linear-gradient(135deg,#1b2a8a,#7b3ac4 55%,#1a1240)"></div><div class="card-body"><div class="meta">by Admin <b>|</b> News</div><h3>Maecenas vestibulum tortor quis nisl semper consectetur.</h3><p>Lorem Ipsum is simply dummy text of the printing and typesetting industry.</p><div class="date">Aug 26, 2021</div></div></article>
  </div>
  <div class="center-btn"><a class="btn" href="#">View all articles</a></div>
</section>

<section class="contact">
  <div class="contact-art" role="img" aria-label="Glowing digital globe with binary code"></div>
  <div class="contact-copy">
    <div class="eyebrow left">Contact</div>
    <h2 class="title">Get in contact<br>with Veltrom</h2>
    <p>Veltrom’s offering is targeted at MSSPs and security solution providers. If you would like information on our prices, apply for a partnership or see a live demo, please contact us using the form below.</p>
    <div class="actions"><a class="btn" href="#">✉ Contact us</a><a class="btn dark" href="#">✎ Arrange a live demo</a></div>
  </div>
</section>

<footer class="footer">
  <div class="f-brand"><div class="logo">VELT<span style="color:var(--gold)">ROM</span></div><small>Follow Us</small><div class="socials"><i></i><i></i><i></i></div></div>
  <div class="f-col" style="left:342px"><h5>About</h5><a href="#">Home</a><a href="#">About</a><a href="#">Q&amp;A</a><a href="#">Pricing</a><a class="active" href="#">Partner Program</a><a href="#">Contact Us</a></div>
  <div class="f-col" style="left:522px"><h5>Resources</h5><a href="#">In the Press</a><a href="#">News</a><a href="#">Screenshots</a><a href="#">Wiki</a><a href="#">Request A Demo</a></div>
  <div class="f-col" style="left:702px"><h5>Contact</h5><div class="lab">Address:</div><div class="val">Lindenweg 12,<br>6300 Seefeld Switzerland</div><div class="lab">Phone:</div><div class="val">+41 700 000 101<br>+41 700 000 202</div><div class="lab">Email:</div><div class="val">info@veltrom.io</div></div>
  <div class="f-col" style="left:882px"><h5>Newsletter</h5><div style="color:var(--muted)">Sign up for cyber threat intelligence alerts</div><div class="newsletter-field"><span>Your Email Address</span><span>✉</span></div></div>
  <div class="f-bottom"><span>© Copyright 2022 VELTROM. All Rights Reserved</span><span><b>PRIVACY POLICY</b><b>IMPRINT</b></span></div>
</footer>

</body>
</html>
```